Dental Business Card

We are looking for a double sided business card that can be easily customized with the names of the different members of our dental team.

I would like the background to be the 2-tone blue fleur-de-lis type pattern on the sides of our website (www.harborvalebrights.com).

I would like the logo attached incorporated.

I would like our address (2847 Birchmont Court, Suite 100, Lakeport, NC 27514), phone number (555-318-4902), fax number (555-318-4977), website (www.harborvalebrights.com), and email address (info@harborvalebrights.com) all included on the front side.

Something a little more artistic to complement/highlight the logo on the back would be interesting.

I would like the business card to look professional, slightly feminine, and expense.

```html
<!DOCTYPE html>
<html lang="en">
<head>
<meta charset="utf-8">
<title>Harborvale Brights – Business Card</title>
<link rel="stylesheet" href="https://fonts.googleapis.com/css2?family=Cinzel:wght@400;600&family=Crimson+Text:wght@400&display=swap">
<style>
  :root {
    --page-bg: #d9dce1;
    --card-paper: #edf1f6;
    --brand-blue: #1c56a6;
    --deep-blue: #0d4aa0;
    --light-blue: #3f8fd9;
    --back-center: #2f8fe6;
    --back-edge: #0b3f9a;
    --white: #ffffff;
  }
  * { margin: 0; padding: 0; box-sizing: border-box; }
  html, body {
    width: 1200px; height: 926px; overflow: hidden;
    background: var(--page-bg);
  }
  .canvas { position: relative; width: 1200px; height: 926px; }
  .card {
    position: absolute; left: 250px; width: 700px; height: 400px;
    overflow: hidden; border-radius: 4px;
    box-shadow: 0 10px 26px rgba(0,0,0,0.22);
  }

  /* Front */
  .card--front { top: 42px; background: var(--card-paper); }
  .card__wave { position: absolute; inset: 0; width: 700px; height: 400px; }
  .practice-heading { position: absolute; left: 44px; top: 34px; width: 310px; }
  .practice-heading__name {
    font-family: "Cinzel", serif; font-weight: 600; font-size: 27px;
    color: var(--brand-blue); letter-spacing: 0.5px; line-height: 1;
  }
  .practice-heading__rule { height: 1px; background: var(--brand-blue); margin: 6px 0 4px; }
  .practice-heading__tagline {
    font-family: "Cinzel", serif; font-size: 12px; color: var(--brand-blue);
    letter-spacing: 1.5px; text-align: right;
  }
  .contact-list { position: absolute; left: 34px; top: 126px; list-style: none; }
  .contact-list__item {
    display: flex; align-items: center; gap: 10px; height: 28px;
    font-family: "Crimson Text", serif; font-size: 20px; color: var(--brand-blue);
  }
  .contact-list__icon { width: 20px; height: 20px; flex: none; }
  .brand-mark {
    position: absolute; right: 46px; top: 110px; width: 250px;
    display: flex; flex-direction: column; align-items: center; gap: 12px;
  }
  .brand-mark__dot { width: 64px; height: 64px; border-radius: 50%; background: var(--light-blue); }
  .brand-mark__name {
    font-family: "Cinzel", serif; font-weight: 600; font-size: 30px;
    color: var(--brand-blue); text-align: center; line-height: 1.1;
  }
  .address {
    position: absolute; left: 30px; bottom: 28px;
    display: flex; align-items: center; gap: 12px;
    font-family: "Cinzel", serif; font-size: 18px; color: var(--white);
    letter-spacing: 1.2px; white-space: nowrap;
  }
  .address__icon { width: 18px; height: 24px; }

  /* Back */
  .card--back {
    top: 484px;
    background: radial-gradient(ellipse at 50% 35%, var(--back-center) 0%, #1f6fd0 45%, var(--back-edge) 100%);
  }
  .back-mark {
    position: absolute; left: 0; right: 0; top: 70px;
    display: flex; flex-direction: column; align-items: center; gap: 14px;
  }
  .back-mark__dot { width: 72px; height: 72px; border-radius: 50%; background: #8cc4f4; }
  .back-mark__name {
    font-family: "Cinzel", serif; font-weight: 600; font-size: 36px;
    color: #0f4fa8; letter-spacing: 1px;
  }
  .back-rule {
    position: absolute; left: 110px; right: 110px; top: 292px;
    height: 1px; background: rgba(255,255,255,0.35);
  }
  .back-website {
    position: absolute; left: 0; right: 0; top: 306px; text-align: center;
    font-family: "Crimson Text", serif; font-size: 22px; color: #dcecfb;
    letter-spacing: 3px;
  }
</style>
</head>
<body>
<main class="canvas">

  <section class="card card--front" aria-label="Business card front">
    <svg class="card__wave" viewBox="0 0 700 400" aria-hidden="true">
      <path d="M0 262 C 170 240, 360 282, 700 330 L700 400 L0 400 Z" fill="var(--light-blue)"/>
      <path d="M0 276 C 180 258, 370 298, 700 340 L700 400 L0 400 Z" fill="var(--card-paper)"/>
      <path d="M0 290 C 190 272, 380 310, 700 348 L700 400 L0 400 Z" fill="var(--deep-blue)"/>
    </svg>

    <header class="practice-heading">
      <div class="practice-heading__name">Harborvale Brights</div>
      <div class="practice-heading__rule"></div>
      <div class="practice-heading__tagline">GENTLE DENTAL CRAFT</div>
    </header>

    <ul class="contact-list">
      <li class="contact-list__item">
        <svg class="contact-list__icon" viewBox="0 0 20 20" aria-label="Phone"><circle cx="10" cy="10" r="10" fill="var(--brand-blue)"/><path d="M5.5 8 Q10 4 14.5 8 L13 9.5 L11.5 8.5 L8.5 8.5 L7 9.5 Z M7 11 H13 V14 H7 Z" fill="#fff"/></svg>
        555-318-4902
      </li>
      <li class="contact-list__item">
        <svg class="contact-list__icon" viewBox="0 0 20 20" aria-label="Fax"><circle cx="10" cy="10" r="10" fill="var(--brand-blue)"/><rect x="5" y="8" width="10" height="6" fill="#fff"/><rect x="7" y="5" width="6" height="3" fill="#fff"/></svg>
        555-318-4977
      </li>
      <li class="contact-list__item">
        <svg class="contact-list__icon" viewBox="0 0 20 20" aria-label="Website"><circle cx="10" cy="10" r="10" fill="var(--brand-blue)"/><rect x="5" y="6" width="10" height="7" rx="1" fill="#fff"/><rect x="8" y="13" width="4" height="2" fill="#fff"/></svg>
        www.harborvalebrights.com
      </li>
      <li class="contact-list__item">
        <svg class="contact-list__icon" viewBox="0 0 20 20" aria-label="Email"><circle cx="10" cy="10" r="10" fill="var(--brand-blue)"/><rect x="5" y="6.5" width="10" height="7" fill="#fff"/><path d="M5 6.5 L10 10.5 L15 6.5" stroke="var(--brand-blue)" stroke-width="1" fill="none"/></svg>
        info@harborvalebrights.com
      </li>
    </ul>

    <div class="brand-mark">
      <div class="brand-mark__dot"></div>
      <div class="brand-mark__name">Harborvale<br>Brights</div>
    </div>

    <p class="address">
      <svg class="address__icon" viewBox="0 0 18 24" aria-label="Location"><path d="M9 0 C4 0 0 4 0 9 C0 15 9 24 9 24 C9 24 18 15 18 9 C18 4 14 0 9 0 Z" fill="#fff"/><circle cx="9" cy="9" r="3.5" fill="var(--deep-blue)"/></svg>
      2847 BIRCHMONT COURT, SUITE 100, LAKEPORT, NC 27514
    </p>
  </section>

  <section class="card card--back" aria-label="Business card back">
    <div class="back-mark">
      <div class="back-mark__dot"></div>
      <div class="back-mark__name">Harborvale Brights</div>
    </div>
    <div class="back-rule"></div>
    <p class="back-website">www.harborvalebrights.com</p>
  </section>

</main>
</body>
</html>
```